Small soho-London based IT Support company website

We've had our logo and stationary redesigned on Sketch Harbor and now we'd like our website done.
We're a small IT support company. Our client base is mainly design studios and advertising agencies working mainly on Zobs.
As such our website needs to be young clean and professional looking.
Our current site can be viewed at http://orvane-lux.it
We currently use Joomla but we're happy to move to Wordpress if that's the only option.

```html
<!DOCTYPE html>
<html lang="en">
<head>
<meta charset="utf-8">
<title>Brisklane – IT Support in Soho</title>
<link href="https://fonts.googleapis.com/css2?family=Questrial&family=Open+Sans:wght@400;600&display=swap" rel="stylesheet">
<style>
:root{
  --olive:#999a36;
  --lime:#cccc00;
  --white:#ffffff;
  --ink:#3a2418;
  --text:#2b2b2b;
  --logo:#b8c200;
}
*{box-sizing:border-box;margin:0;padding:0}
html,body{width:1200px;height:1050px;overflow:hidden}
body{position:relative;background:var(--white);font-family:"Questrial",sans-serif;color:var(--text)}
.band{position:absolute;left:0;width:1200px}
.abs{position:absolute}
.brand{left:248px;top:106px;font-family:"Questrial",sans-serif;font-size:54px;color:var(--logo);letter-spacing:1px;display:flex;align-items:center;gap:14px}
.brand-dot{width:14px;height:14px;border-radius:50%;background:var(--logo)}
.phone-line{left:714px;top:120px;display:flex;align-items:center;gap:10px;font-size:29px;color:#222;font-family:"Questrial",sans-serif;letter-spacing:.5px}
.nav{left:239px;top:195px;width:472px;height:31px;border-radius:6px;background:linear-gradient(#fdfdfd,#dcdcdc);box-shadow:0 2px 3px rgba(0,0,0,.3);display:flex;font-family:"Open Sans",sans-serif;font-size:12.5px}
.nav a{color:#222;text-decoration:none;display:flex;align-items:center;justify-content:center;border-right:1px solid #a8a8a8}
.nav a:last-child{border-right:none}
.slider{left:238px;top:235px;width:473px;height:148px;border:1px solid #c8c8c8;border-radius:3px;background:radial-gradient(ellipse at 28% 25%,#f2f2f2 0%,#c9cbcd 45%,#a0a3a6 100%)}
.welcome{left:241px;top:396px;white-space:nowrap}
.welcome h1{font-size:13.5px;color:var(--ink);letter-spacing:.5px;margin-bottom:12px;font-weight:600;font-family:"Open Sans",sans-serif}
.welcome p{font-size:11px;line-height:12.5px;color:var(--ink);letter-spacing:.1px}
.device{left:778px;top:198px;width:128px;height:239px;border-radius:20px;background:linear-gradient(90deg,#2a2a2a,#555 50%,#2a2a2a);border:2px solid #c9c9c9}
.screen{position:absolute;left:5px;top:34px;width:110px;height:165px;background:#fff;font-family:Georgia,serif;font-size:7.5px;color:#333;padding:6px 9px;white-space:nowrap}
.row{display:flex;justify-content:space-between;align-items:center;height:22px}
.field{width:42px;height:15px;border:1px solid #aaa;font-size:7px;padding-left:2px;line-height:13px}
.check{display:flex;align-items:center;gap:6px;height:15px}
.check i{width:10px;height:10px;border:1px solid #999;display:block}
.estimate{margin-top:8px}
.est-box{border:1px solid #aaa;height:13px;margin-top:2px;font-size:7px;padding-left:2px}
.learn{text-align:right;color:#1a3bd6;text-decoration:underline;margin-top:10px;font-size:6.5px}
.home-btn{position:absolute;left:52px;top:206px;width:20px;height:20px;border-radius:50%;background:#111;border:1px solid #555}
.speaker{position:absolute;left:49px;top:17px;width:26px;height:3px;border-radius:2px;background:#111}
.card{top:473px;width:232px;height:236px;background:linear-gradient(#f2f2f2,#fff 40%);border:1px solid #e2e2e2;border-radius:3px;box-shadow:0 2px 4px rgba(0,0,0,.15);padding:12px 4px 0 18px;font-size:9px;letter-spacing:.3px;line-height:10.8px;color:#222;white-space:nowrap;overflow:hidden}
.card h2{font-size:14px;font-weight:400;margin:10px 0 4px;letter-spacing:.4px}
.card p{margin-bottom:11px}
.card ul{list-style:none}
.card li::before{content:"";display:inline-block;width:5px;height:5px;border-radius:50%;background:#111;margin-right:4px;vertical-align:1px}
.icons{display:flex;gap:20px;height:32px;align-items:center}
.mark-circle{width:26px;height:26px;border-radius:50%;background:#bfc3c6}
.mark-square{width:26px;height:26px;background:#7aa4d8}
.location{left:255px;top:737px;color:#222;font-size:11.5px;line-height:13.5px;letter-spacing:.3px;white-space:nowrap}
.location h2{font-size:13px;font-family:"Open Sans",sans-serif;font-weight:600;margin-bottom:14px;letter-spacing:.8px}
.location p{margin-bottom:13px}
.postcode{left:297px;top:879px;font-size:7.5px;color:#fff;font-family:"Open Sans",sans-serif;white-space:nowrap}
.postcode-input{left:303px;top:897px;width:56px;height:14px;border-radius:3px;background:#fff;border:3px solid #c8c8c8}
.postcode-go{left:362px;top:897px;width:14px;height:14px;border-radius:50%;background:#8a8a8a}
.map{left:493px;top:734px;width:444px;height:224px;background:linear-gradient(135deg,#ebe6dc,#e3ddcf 50%,#f1d9a0)}
.copyright{left:263px;top:983px;font-size:10.5px;letter-spacing:.8px;color:#333;white-space:nowrap}
.copyright b{color:var(--logo);font-weight:400}
.footer-nav{left:599px;top:984px;font-family:"Open Sans",sans-serif;font-size:10px;color:#222;display:flex;gap:10px;white-space:nowrap}
</style>
</head>
<body>
<div class="band" style="top:0;height:88px;background:var(--olive)"></div>
<div class="band" style="top:174px;height:336px;background:var(--olive)"></div>
<div class="band" style="top:510px;height:93px;background:var(--lime)"></div>
<div class="band" style="top:603px;height:62px;background:var(--olive)"></div>
<div class="band" style="top:665px;height:12px;background:var(--lime)"></div>
<div class="band" style="top:722px;height:141px;background:var(--lime)"></div>
<div class="band" style="top:863px;height:110px;background:var(--olive)"></div>

<header>
  <div class="abs brand"><span>Brisklane</span><span class="brand-dot"></span></div>
  <div class="abs phone-line">
    <svg width="22" height="22" viewBox="0 0 22 22"><rect width="22" height="22" rx="3" fill="#b8c200"/><path d="M7 5c1 0 2 2 2 3s-1 1-1 2 3 4 4 4 1-1 2-1 3 1 3 2-1 2-2 2C9 17 5 12 5 7c0-1 1-2 2-2z" fill="#fff"/></svg>
    <span>0203 555 01 47</span>
  </div>
</header>

<nav class="abs nav">
  <a href="#" style="width:88px">Home</a>
  <a href="#" style="width:100px">About us</a>
  <a href="#" style="width:95px">Services</a>
  <a href="#" style="width:78px">Why us</a>
  <a href="#" style="width:111px">Contact us</a>
</nav>

<div class="abs slider" role="img" aria-label="Featured banner slideshow">
  <svg class="abs" style="left:440px;top:12px" width="16" height="124" viewBox="0 0 16 124">
    <path d="M2 10 8 4 14 10" stroke="#fff" stroke-width="3" fill="none"/>
    <g fill="#fff"><circle cx="8" cy="22" r="1.5"/><circle cx="8" cy="32" r="1.5"/><circle cx="8" cy="42" r="1.5"/><circle cx="8" cy="52" r="1.5"/><circle cx="8" cy="62" r="1.5"/><circle cx="8" cy="72" r="1.5"/><circle cx="8" cy="82" r="1.5"/><circle cx="8" cy="92" r="1.5"/><circle cx="8" cy="102" r="1.5"/></g>
    <path d="M2 114 8 120 14 114" stroke="#fff" stroke-width="3" fill="none"/>
  </svg>
</div>

<section class="abs welcome">
  <h1>Welcome</h1>
  <p>We're Brisklane. Located in Soho - London, trusted by small medium and large companies<br>to provide quick effective responses to their technical needs.<br>We are the West End's outsourced IT department.</p>
</section>

<aside class="abs device">
  <div class="speaker"></div>
  <div class="screen">
    <div class="row"><span>laptops</span><span class="field">0</span></div>
    <div class="row"><span>desktops</span><span class="field">0</span></div>
    <div class="row"><span>servers</span><span class="field">0</span></div>
    <div class="check"><i></i>remote support</div>
    <div class="check"><i></i>server monitoring</div>
    <div class="estimate">Monthly estimate<div class="est-box">£ 0</div></div>
    <div class="learn">Learn more</div>
  </div>
  <div class="home-btn"></div>
</aside>

<section class="abs card" style="left:236px">
  <div class="icons"><span class="mark-circle"></span></div>
  <h2>ZOB</h2>
  <p>We have over 50 combined years<br>in supporting Zob systems.</p>
  <p>Our Zob specialists speak plain<br>English so you're not left baffled by<br>computer jargon.</p>
  <ul><li>SME &amp; Corporate Networks</li><li>Corvel Email Server</li><li>Bespoke Applications</li><li>Web Services</li><li>Connectivity</li><li>Security</li></ul>
</section>

<section class="abs card" style="left:479px">
  <div class="icons"><span class="mark-square"></span></div>
  <h2>PC</h2>
  <p>Friendly Quorix techs with years<br>of industry experience.</p>
  <ul><li>Quorix Server OS</li><li>PC &amp; Laptop Applications</li><li>Hardware Upgrades</li><li>Antivirus &amp; Spam</li><li>Firewall Security</li><li>Email Filtering</li><li>Networking</li><li>Backups</li></ul>
</section>

<section class="abs card" style="left:721px">
  <div class="icons"><span class="mark-circle"></span><span class="mark-square"></span></div>
  <h2>Combined</h2>
  <p>Using both Zobs &amp; PC's can be tricky<br>but not with us.</p>
  <p>Brisklane is a joint venture between two IT<br>directors, one Zob focused and one PC<br>focused but both with proven track<br>records in running successful<br>IT supports firms.</p>
  <p>Our engineers are specialists not all<br>rounders.<br>This means you get the correct fix not<br>a hack.</p>
</section>

<section class="abs location">
  <h2>Location</h2>
  <p>This map shows where we are,<br>smack bang in the middle of Soho<br>and Covent Garden.</p>
  <p>Type your postcode in to see how<br>close we are to your offices.</p>
</section>
<div class="abs postcode">ENTER YOUR POSTCODE</div>
<div class="abs postcode-input"></div>
<div class="abs postcode-go"></div>

<div class="abs map" role="img" aria-label="Street map of Soho and Covent Garden showing the office location"></div>

<footer>
  <div class="abs copyright">© <b>Brisklane</b> Ltd 2011</div>
  <div class="abs footer-nav"><span>Home</span><span>|</span><span>About us</span><span>|</span><span>Services</span><span>|</span><span>Why us</span><span>|</span><span>Contact us</span><span>|</span><span>RSS</span></div>
</footer>
</body>
</html>
```